依頼詳細
当サイトに店舗情報等を掲載してもらうための店舗への説明用チラシのデザイン制作をお願い致します。思わず掲載をしたくなるようなデザインをお願いします。シンプルでわかり易いものが希望です。
記載項目
サイト名はsemu(セム)・店舗情報掲載料1P21,000円/年額 複数P(写真・メニュー・クーポン等)42,000円/年額 求人情報掲載無料・採用時31,500円 当サイトの収益は児童養護施設等の子供達の学習支援に使われます。
サイズ
A4
ページ数
片面
希望イメージ
シンプル 複雑
単色 カラフル
暗い 明るい
日常 高級
遊び心 厳粛
未来的 伝統的
女性的 男性的
希望する色
オレンジ
納品ファイル
• 高解像度JPG (.jpg)
• イラストレーター形式 (.ai)
補足説明
《選ぶワクワクを全ての人に》をミッションにしたNPOです。この度開設するサイトを通じて、大人の生活の選択肢を増やし、学習支援によって子どもの将来の選択肢を増やすことを目的としています。サイト開設にあたっては、一定数の店舗登録が必須なため、店舗への説明がわかりやすい営業用チラシが必要です。イメージとしてはひらけ堂やぽみたすが近いかと思います。

```html
<!DOCTYPE html>
<html lang="ja">
<head>
<meta charset="utf-8">
<title>semu 掲載店募集チラシ</title>
<link href="https://fonts.googleapis.com/css2?family=Noto+Sans+JP:wght@400;500;700;900&family=M+PLUS+Rounded+1c:wght@500;700;800&display=swap" rel="stylesheet">
<style>
:root{
  --orange:#f08a1c;
  --orange-deep:#e8620f;
  --red:#e5392a;
  --pink:#ec6fa0;
  --yellow:#f5b31b;
  --green:#7cb82f;
  --green-deep:#5a9a1e;
  --blue:#2a8fd6;
  --ink:#4a3a2e;
  --paper:#fffdf8;
  --cream:#fdf1e0;
}
*{margin:0;padding:0;box-sizing:border-box}
html,body{width:857px;height:1200px;overflow:hidden;background:#fff}
.flyer{position:relative;width:857px;height:1200px;background:var(--paper);font-family:"Noto Sans JP",sans-serif;color:var(--ink);overflow:hidden}
.abs{position:absolute}

.photo-hands{left:0;top:0;width:300px;height:250px;background:linear-gradient(135deg,#f7e6d6,#fff8f0 80%);opacity:.9}
.photo-woman{left:600px;top:0;width:257px;height:380px;background:linear-gradient(180deg,#e9e1d8,#cfc2b3)}
.mission{left:60px;top:20px;font-family:"M PLUS Rounded 1c",sans-serif;font-weight:800;font-size:40px;color:var(--orange-deep);letter-spacing:1px}
.mission-lead{left:60px;top:78px;width:560px;font-size:17px;line-height:1.65;font-weight:500}
.open-date{left:150px;top:186px;width:440px;height:44px;border:2px solid var(--orange);border-radius:22px;background:#fff;color:var(--orange-deep);font-weight:700;font-size:22px;display:flex;align-items:center;justify-content:center}

.photo-dish{left:0;top:245px;width:315px;height:300px;background:radial-gradient(circle at 45% 50%,#e9553b,#f2a65a 55%,#f7e2c4)}
.portal-label{left:345px;top:258px;font-size:22px;font-weight:700}
.brand{left:400px;top:290px;display:flex;align-items:baseline;gap:14px;color:var(--orange)}
.brand-name{font-family:"M PLUS Rounded 1c",sans-serif;font-weight:800;font-size:84px;letter-spacing:4px;line-height:1}
.brand-kana{font-family:"M PLUS Rounded 1c",sans-serif;font-weight:800;font-size:28px}
.brand-url{left:345px;top:390px;font-size:22px;font-weight:700;color:var(--orange-deep)}

.categories{left:322px;top:430px;display:flex;gap:6px}
.categories span{display:block;width:90px;height:32px;border-radius:4px;color:#fff;font-weight:700;font-size:15px;text-align:center;line-height:32px}
.cat-food{background:var(--red)}
.cat-beauty{background:var(--pink)}
.cat-fun{background:var(--orange)}
.cat-help{background:var(--yellow)}
.cat-work{background:var(--green)}

.pitch{left:335px;top:482px;width:400px;font-size:19px;line-height:1.6;font-weight:500}
.recruit-badge{left:752px;top:480px;width:96px;height:96px;border-radius:50%;background:var(--blue);color:#fff;font-weight:900;font-size:22px;line-height:1.2;display:flex;align-items:center;justify-content:center;text-align:center}

.site-preview{left:28px;top:575px;width:390px;height:500px;border-radius:6px;background:linear-gradient(180deg,#f6d7a6,#fbeed9 30%,#f3f3f3 60%,#e9e1d3)}
.preview-note{left:30px;top:1080px;font-size:14px}

.fee-title{left:430px;top:572px;width:410px;height:40px;background:var(--orange);color:#fff;font-weight:900;font-size:22px;line-height:40px;padding-left:18px}
.fees{left:440px;top:625px;width:400px}
.fee{margin-bottom:12px}
.fee-name{font-size:19px;font-weight:700}
.fee-price{text-align:right;color:var(--orange-deep);font-weight:900;font-size:44px;line-height:1.05}
.fee-price small{font-size:18px;color:var(--ink);font-weight:700;margin-left:4px}
.fee-free{display:flex;align-items:baseline;justify-content:flex-end;gap:10px;color:var(--orange-deep);font-weight:900;font-size:44px;line-height:1.05}
.fee-free small{font-size:17px;color:var(--ink);font-weight:700}
.proceeds{left:440px;top:925px;width:400px;font-size:14.5px;line-height:1.55;font-weight:500}

.townscape{left:430px;top:980px;width:427px;height:120px;background:linear-gradient(180deg,rgba(255,255,255,0),#e3eef4);opacity:.9}

.contact{left:0;top:1110px;width:857px;height:90px;background:var(--green)}
.contact-call{left:16px;top:1124px;width:130px;height:62px;background:var(--yellow);color:var(--ink);font-weight:900;font-size:15px;line-height:1.35;display:flex;align-items:center;justify-content:center;text-align:center;border-radius:4px}
.contact-tel{left:160px;top:1116px;color:#fff;font-weight:900;font-size:46px;display:flex;align-items:center;gap:10px;letter-spacing:1px}
.contact-small{left:162px;top:1172px;color:#fff;font-size:12px}
.operator{left:645px;top:1130px;color:#fff;font-size:14px;line-height:1.6;font-weight:700}
</style>
</head>
<body>
<div class="flyer">
  <div class="abs photo-hands" role="img" aria-label="器を手にする人の写真"></div>
  <div class="abs photo-woman" role="img" aria-label="微笑む女性の写真"></div>
  <h1 class="abs mission">選ぶワクワクを全ての人に。</h1>
  <p class="abs mission-lead">わたしたちは「semu(セム)」を通じて、大人の生活の選択肢を増やし、学習支援によって子どもの将来の選択肢を増やすことを目的としています。</p>
  <div class="abs open-date">2014.0.0(日)サイトOPEN予定</div>

  <div class="abs photo-dish" role="img" aria-label="パスタ料理の写真"></div>
  <p class="abs portal-label">八代市の地域情報ポータルサイト</p>
  <div class="abs brand"><span class="brand-name">semu</span><span class="brand-kana">セム</span></div>
  <p class="abs brand-url">http://www.semu-xxxxxxxx.com</p>
  <div class="abs categories">
    <span class="cat-food">ごちそう</span>
    <span class="cat-beauty">きれいになる</span>
    <span class="cat-fun">たのしむ</span>
    <span class="cat-help">おやくだち</span>
    <span class="cat-work">はたらく</span>
  </div>
  <p class="abs pitch">地域のイベント情報や店舗情報など様々なコンテンツを掲載します。あなたのお店をPRしてみませんか？</p>
  <div class="abs recruit-badge">掲載店<br>募集中!</div>

  <div class="abs site-preview" role="img" aria-label="サイト画面のイメージ"></div>
  <p class="abs preview-note">※サイトイメージ</p>

  <h2 class="abs fee-title">ご掲載料金</h2>
  <div class="abs fees">
    <div class="fee">
      <p class="fee-name">店舗情報掲載料１ページ</p>
      <p class="fee-price">21,000円<small>/年額</small></p>
    </div>
    <div class="fee">
      <p class="fee-name">複数ページ(写真・メニュー・クーポン等)</p>
      <p class="fee-price">42,000円<small>/年額</small></p>
    </div>
    <div class="fee">
      <p class="fee-name">求人情報掲載</p>
      <p class="fee-free">無料<small>(採用時 31,500円)</small></p>
    </div>
  </div>
  <p class="abs proceeds">※当サイトの収益は児童養護施設等の子供達の学習支援に使われます。</p>
  <div class="abs townscape" role="img" aria-label="街並みのイラスト"></div>

  <div class="abs contact"></div>
  <div class="abs contact-call">まずはお気軽に<br>お問い合わせ<br>ください</div>
  <div class="abs contact-tel">
    <svg width="40" height="40" viewBox="0 0 24 24" aria-hidden="true"><path fill="#fff" d="M6.6 10.8a15 15 0 0 0 6.6 6.6l2.2-2.2c.3-.3.7-.4 1-.2 1.1.4 2.3.6 3.6.6.6 0 1 .4 1 1V20c0 .6-.4 1-1 1A17 17 0 0 1 3 4c0-.6.4-1 1-1h3.5c.6 0 1 .4 1 1 0 1.3.2 2.5.6 3.6.1.3 0 .7-.2 1z"/></svg>
    TEL.096-000-0000
  </div>
  <p class="abs contact-small">FAX.096-000-0001　〒866-0000 八代市本町0-0</p>
  <p class="abs operator">semu(セム)<br>運営会社 ○○○○</p>
</div>
</body>
</html>
```